We need a label for a new company based in Marlbrough, New Zealand. We produce a selection of fusion honey* from a single block that is infulenced by a pristine spring feed stream. (*fusion honey is: is manuka,kanuka,blue borate, lucerne, white clover and wild flowers. Kanuka and manuka are renowned for thier healing properties.

The label needs to contain
1. The label needs to inculde a logo of your design based off your conception of above info.
2. Nutritional facts. (please see attached file for info)
3. 320g (this is the weight of the honey)
4. Made in New Zealand by Harlow Knoll Apiaries Ltd, Awatere Valley, Marlbrough.
5. Ingredients: 100% Honey
6. www.quillbrookhoney.nz
7. Where the bee's are mild and the keepers are wild
8. Our blurb:
Quillbrook Honey is produced within a single block that nestles in the Awatere Valley of Marlborough, New Zealand. The bees are gifted with a wild nectar source of Manuka, Kanuka, Wildflowers, Blue Borage, White Clover and Lucerne.

Target Market(s)

Health conscious New Zealanders who are interested in artisan honey.

Requirements
Must have
• Clear, simple layout that has a touch of quirkiness.

```html
<!DOCTYPE html>
<html lang="en">
<head>
<meta charset="utf-8">
<title>Quillbrook Honey – Jar Label</title>
<link href="https://fonts.googleapis.com/css2?family=Oswald:wght@500&family=Roboto:wght@300;400&family=Dancing+Script:wght@400&family=Marcellus&display=swap" rel="stylesheet">
<style>
  :root {
    --cream: #fdf59c;
    --bark: #4a3f22;
    --bark-soft: #6a5c33;
    --gold: #f5b915;
    --honey-light: #ffd21c;
    --honey-deep: #f39a06;
    --ink: #3b3320;
    --white: #ffffff;
    --badge-green: #58b847;
    --flag-red: #c8102e;
    --flag-blue: #1f3f8f;
  }
  * { box-sizing: border-box; margin: 0; padding: 0; }
  html, body { width: 1200px; height: 1000px; overflow: hidden; background: var(--white); }
  .canvas { position: relative; width: 1200px; height: 1000px; }

  .label {
    position: absolute; left: 25px; top: 97px;
    width: 1153px; height: 360px;
    background: var(--cream);
    color: var(--ink);
    font-family: "Roboto", sans-serif;
  }

  /* left panel */
  .blurb {
    position: absolute; left: 52px; top: 86px; width: 234px;
    border: 1.5px solid var(--ink);
    padding: 9px 8px;
    font-size: 11.6px; line-height: 1.45; text-align: center; font-weight: 300;
  }
  .blurb strong { font-family: "Oswald", sans-serif; font-weight: 500; letter-spacing: .3px; }
  .maker { position: absolute; left: 62px; top: 262px; display: flex; gap: 15px; align-items: flex-start; }
  .origin-badge { width: 46px; height: 46px; border-radius: 50%; background: var(--flag-blue); border: 3px solid var(--flag-red); flex: none; }
  .maker-text { font-size: 10px; line-height: 1.35; font-weight: 300; }
  .maker-name { font-family: "Marcellus", serif; font-size: 15px; display: block; margin: 2px 0 1px; }
  .website { position: absolute; left: 86px; top: 326px; font-family: "Marcellus", serif; font-size: 14.5px; letter-spacing: .3px; }

  /* foliage bands */
  .foliage { position: absolute; top: 0; height: 360px; width: 104px; }
  .foliage-left { left: 313px; background: linear-gradient(90deg, rgba(74,63,34,0) 0%, rgba(74,63,34,.55) 35%, var(--bark) 85%); }
  .foliage-right { left: 729px; background: linear-gradient(270deg, rgba(74,63,34,0) 0%, rgba(74,63,34,.55) 35%, var(--bark) 85%); }

  /* front panel */
  .front { position: absolute; left: 416px; top: 0; width: 313px; height: 360px; background: var(--bark); overflow: hidden; }
  .drip {
    position: absolute; left: 0; top: 0; width: 313px; height: 100px;
    background: linear-gradient(180deg, var(--honey-light) 0%, var(--honey-deep) 55%, var(--bark) 100%);
  }
  .logo { position: absolute; left: 76px; top: 86px; width: 160px; height: 160px; }
  .logo-name {
    position: absolute; inset: 0;
    display: flex; align-items: center; justify-content: center; text-align: center;
    font-family: "Oswald", sans-serif; font-weight: 500; font-size: 22px; line-height: 1.15;
    letter-spacing: 1px; color: var(--gold);
  }
  .tagline {
    position: absolute; left: 0; top: 280px; width: 313px; text-align: center;
    font-family: "Dancing Script", cursive; font-size: 15px; line-height: 1.3; color: var(--white);
  }
  .natural-badge { position: absolute; left: 244px; top: 303px; width: 45px; height: 45px; border-radius: 50%; background: var(--badge-green); border: 2px solid var(--white); }
  .weight { position: absolute; left: 0; top: 334px; width: 313px; text-align: center; font-family: "Marcellus", serif; font-size: 12px; color: var(--gold); letter-spacing: .5px; }

  /* nutrition */
  .nutrition { position: absolute; left: 860px; top: 71px; width: 236px; border: 1px solid var(--ink); border-collapse: collapse; font-size: 9.6px; font-weight: 300; }
  .nutrition caption { background: var(--bark); color: var(--white); font-size: 12px; line-height: 15px; border: 1px solid var(--ink); border-bottom: 0; }
  .nutrition td { padding: 1px 2px; vertical-align: top; line-height: 1.35; }
  .nutrition tr { border-bottom: 1px solid var(--ink); }
  .nutrition .num { text-align: right; padding-right: 4px; }
  .nutrition .plain { border-bottom: 0; }
  .ingredients { position: absolute; left: 860px; top: 276px; font-size: 10px; font-weight: 400; }
</style>
</head>
<body>
<main class="canvas">
  <section class="label">
    <p class="blurb"><strong>QUILLBROOK HONEY</strong> is produced within a single block that nestles in the Awatere Valley of Marlborough, New Zealand. The bees are gifted with a wild nectar source of Manuka, Kanuka, Wildflowers, Blue Borage, White Clover and Lucerne.</p>

    <div class="maker">
      <span class="origin-badge" role="img" aria-label="Made in New Zealand badge"></span>
      <p class="maker-text">Made in New Zealand by<span class="maker-name">Harlow Knoll Apiaries Ltd,</span>Awatere Valley, Marlbrough.</p>
    </div>
    <p class="website">www.quillbrookhoney.nz</p>

    <div class="foliage foliage-left" role="img" aria-label="Silhouette of native leaves and blossoms"></div>
    <div class="foliage foliage-right" role="img" aria-label="Silhouette of native leaves and blossoms"></div>

    <div class="front">
      <div class="drip" role="img" aria-label="Honey dripping from the top edge"></div>

      <div class="logo">
        <svg width="160" height="160" viewBox="0 0 160 160" aria-hidden="true">
          <circle cx="80" cy="80" r="76" fill="none" stroke="var(--gold)" stroke-width="4"/>
        </svg>
        <p class="logo-name">QUILLBROOK<br>HONEY</p>
      </div>

      <p class="tagline">Where the bee's are wild and<br>the keepers are wild</p>
      <span class="natural-badge" role="img" aria-label="100% natural badge"></span>
      <p class="weight">NT WT 320 GRAM</p>
    </div>

    <table class="nutrition">
      <caption>Nutrition Facts</caption>
      <tr><td colspan="3">Serving Per 1 Tablespoon (20g)</td></tr>
      <tr class="plain"><td>Energy</td><td>Qty Per Serving</td><td>Qty Per Serving</td></tr>
      <tr><td></td><td>1kg<br>272kj<br>(65 Cal)</td><td>100g<br>1404kj<br>(335Cal)</td></tr>
      <tr><td>Protein</td><td class="num">&lt;1g</td><td class="num">&lt;1g</td></tr>
      <tr><td>Fat (total)</td><td class="num">0g</td><td class="num">0g</td></tr>
      <tr><td>&gt;Saturated</td><td class="num">0g</td><td class="num">0g</td></tr>
      <tr><td>Carbohydrat</td><td class="num">16g</td><td class="num">82.1g</td></tr>
      <tr><td>&gt;Sugars</td><td class="num">16g</td><td class="num">82.1g</td></tr>
      <tr><td>Sodium</td><td class="num">2.8mg</td><td class="num">14mg</td></tr>
    </table>
    <p class="ingredients">Ingredients: 100% Honey</p>
  </section>
</main>
</body>
</html>
```